Surface Protection company needs cards

We are a New Zealand company that will apply nanotechnology coatings on surfaces to prevent growth and spread of bacteria, viruses, mold etc with a sprayer. We deal with large corporates, airlines, hospitals and schools so we are after a new modern, simple and clean look that will have great visual impact.
We a company that is focused on prevention and protection.

Company name, Vela Shield

Subtext, Antimicrobial Surface Protection

Logo, VS

Target Market(s)

Hospitals, Transport agencies, Airlines, Corporate entities

Contact Information for Business Card

Company name, VelaShield
Logo, VS

Gareth Tolley
velashieldnz@postbox.example
+64219305562
www.velashield.example.nz

Requirements
Must have
• Simple clean look.
Nice to have
• We apply nano coatings so try and incorporate this into a theme somehow

```html
<!DOCTYPE html>
<html lang="en">
<head>
<meta charset="utf-8">
<title>Vela Shield — Business Card</title>
<link rel="stylesheet" href="https://fonts.googleapis.com/css2?family=Montserrat:wght@500;600&display=swap">
<style>
  :root {
    --backdrop: #1e1e1e;
    --card: #f8f8f8;
    --brand: #2a1b5b;
    --ink: #111111;
    --ink-soft: #333333;
    --icon: #2b2b2b;
  }
  * { box-sizing: border-box; margin: 0; padding: 0; }
  html, body {
    width: 1200px; height: 1200px; overflow: hidden;
    background: var(--backdrop);
    font-family: "Montserrat", sans-serif;
  }
  .card {
    position: absolute; left: 227px;
    width: 747px; height: 432px;
    background: var(--card);
    overflow: hidden;
  }
  .card--front { top: 107px; }
  .card--back { top: 623px; }

  .card__bands { position: absolute; left: 0; top: 0; width: 747px; height: 432px; }

  .front__monogram {
    position: absolute; left: 0; width: 100%; top: 98px;
    text-align: center;
    font-size: 180px; font-weight: 600; line-height: 1;
    color: var(--brand); letter-spacing: -4px;
  }
  .front__url {
    position: absolute; left: 0; width: 100%; top: 302px;
    text-align: center;
    font-size: 25px; font-weight: 500; color: var(--ink);
  }

  .back__divider {
    position: absolute; left: 338px; top: 45px;
    width: 4px; height: 344px;
    background: linear-gradient(to bottom, rgba(0,0,0,0), rgba(0,0,0,0.45) 30%, rgba(0,0,0,0.45) 70%, rgba(0,0,0,0));
    filter: blur(1px);
    border-radius: 2px;
  }
  .brand {
    position: absolute; left: 25px; top: 160px; width: 290px;
  }
  .brand__name {
    font-size: 52px; font-weight: 500; line-height: 1;
    color: var(--brand); letter-spacing: -0.5px;
  }
  .brand__tagline {
    margin-top: 4px;
    font-size: 17px; font-weight: 500; color: var(--ink-soft);
    white-space: nowrap;
  }

  .contact__name {
    position: absolute; left: 419px; top: 62px;
    font-size: 35px; font-weight: 500; color: var(--ink);
  }
  .contact__list { list-style: none; }
  .contact__item {
    position: absolute; left: 371px; height: 24px;
    display: flex; align-items: center;
    font-size: 19px; font-weight: 500; color: var(--ink);
    white-space: nowrap;
  }
  .contact__icon { width: 23px; height: 23px; margin-right: 25px; flex: none; }
  .contact__item--phone { top: 138px; }
  .contact__item--email { top: 200px; }
  .contact__item--web { top: 264px; }
</style>
</head>
<body>

<section class="card card--front">
  <svg class="card__bands" viewBox="0 0 747 432" aria-hidden="true">
    <polygon points="0,393 289,393 338,414 0,414" fill="var(--brand)"/>
    <rect x="0" y="419" width="747" height="6" fill="var(--brand)"/>
  </svg>
  <div class="front__monogram">VS</div>
  <p class="front__url">www.velashield.example.nz</p>
</section>

<section class="card card--back">
  <svg class="card__bands" viewBox="0 0 747 432" aria-hidden="true">
    <polygon points="376,394 747,394 747,414 314,414" fill="var(--brand)"/>
    <rect x="0" y="419" width="747" height="6" fill="var(--brand)"/>
  </svg>

  <div class="brand">
    <div class="brand__name">VelaShield</div>
    <div class="brand__tagline">Antimicrobial Surface Protection</div>
  </div>

  <div class="back__divider"></div>

  <h1 class="contact__name">Gareth Tolley</h1>
  <ul class="contact__list">
    <li class="contact__item contact__item--phone">
      <svg class="contact__icon" viewBox="0 0 23 23" aria-hidden="true">
        <rect width="23" height="23" fill="var(--icon)"/>
        <rect x="8" y="3.5" width="7" height="16" rx="1.5" fill="none" stroke="#fff" stroke-width="1"/>
        <line x1="9" y1="5.5" x2="14" y2="5.5" stroke="#fff" stroke-width="0.8"/>
        <line x1="9" y1="17" x2="14" y2="17" stroke="#fff" stroke-width="0.8"/>
      </svg>
      +64219305562
    </li>
    <li class="contact__item contact__item--email">
      <svg class="contact__icon" viewBox="0 0 23 23" aria-hidden="true">
        <rect width="23" height="23" fill="var(--icon)"/>
        <rect x="3.5" y="6" width="16" height="11" fill="#fff"/>
        <polyline points="3.5,6 11.5,12.5 19.5,6" fill="none" stroke="var(--icon)" stroke-width="0.8"/>
        <line x1="3.5" y1="17" x2="9.5" y2="11" stroke="var(--icon)" stroke-width="0.6"/>
        <line x1="19.5" y1="17" x2="13.5" y2="11" stroke="var(--icon)" stroke-width="0.6"/>
      </svg>
      velashieldnz@postbox.example
    </li>
    <li class="contact__item contact__item--web">
      <svg class="contact__icon" viewBox="0 0 23 23" aria-hidden="true">
        <rect width="23" height="23" fill="var(--icon)"/>
        <g fill="none" stroke="#fff" stroke-width="0.9">
          <circle cx="11.5" cy="11.5" r="7.5"/>
          <ellipse cx="11.5" cy="11.5" rx="3.2" ry="7.5"/>
          <line x1="11.5" y1="4" x2="11.5" y2="19"/>
          <line x1="4" y1="11.5" x2="19" y2="11.5"/>
          <line x1="5" y1="8" x2="18" y2="8"/>
          <line x1="5" y1="15" x2="18" y2="15"/>
        </g>
      </svg>
      www.velashield.example.nz
    </li>
  </ul>
</section>

</body>
</html>
```